New, clean letterhead for law firm in Colorado using recently designed logo.

Professional letterhead for established law firm rebranding. We service high end clientele with mostly family law and personal injury cases. Need source files for future changes. Prefer logo at top, names of members and staff in left margin, contact info in footer.

Target Market(s)

High wealth individuals

Contact Information for Business Card

Need options for traditional and square two sided business cards

Font styles to use
Serif

Colors
0555a3

Requirements
Must have
• Our logo; blue, gray, and white; modern feel.
Should not have
• Images of people

```html
<!DOCTYPE html>
<html lang="en">
<head>
<meta charset="utf-8">
<title>Alder Crest Law – Stationery</title>
<link href="https://fonts.googleapis.com/css2?family=Open+Sans:wght@400;600&display=swap" rel="stylesheet">
<style>
:root{
  --brand-blue:#0555a3;
  --card-blue:#1f64b4;
  --ink:#555b63;
  --muted:#8a9099;
  --rule:#4a6f9a;
  --paper:#f7f9fb;
  --backdrop:#e7e7e7;
  --white:#ffffff;
}
*{margin:0;padding:0;box-sizing:border-box}
html,body{width:1200px;height:801px;overflow:hidden;background:var(--backdrop);font-family:"Open Sans",sans-serif;color:var(--ink)}
.stage{position:relative;width:1200px;height:801px}

/* Letterhead */
.letterhead{position:absolute;left:250px;top:101px;width:432px;height:611px;background:var(--paper);box-shadow:0 1px 4px rgba(0,0,0,.12)}
.brand{position:absolute;display:flex;align-items:center;gap:6px;color:var(--brand-blue);font-weight:600;letter-spacing:.4px;white-space:nowrap}
.brand .mark{border-radius:50%;background:var(--brand-blue);flex:none}
.letterhead .brand{left:31px;top:56px;font-size:10px}
.letterhead .brand .mark{width:10px;height:10px}

.team{position:absolute;left:31px;width:81px;font-size:6.4px;line-height:8.6px;color:var(--muted)}
.team .rule{height:1px;background:var(--rule);margin-bottom:16px}
.team .member{margin-bottom:9.5px}
.team-a{top:124px}
.team-b{top:221px}

.letter{position:absolute;left:146px;top:124px;width:266px;font-size:8px;line-height:10.5px}
.letter .salutation{font-weight:600;margin-bottom:16px}
.letter p{margin-bottom:15px}

.footer{position:absolute;left:31px;right:31px;top:571px;display:flex;font-size:6.6px;line-height:9px;color:var(--muted)}
.footer .col{padding-right:14px}
.footer .col+.col{border-left:1px solid var(--muted);padding-left:26px}
.footer .phones{width:104px}
.footer .address{width:145px}
.footer strong{color:var(--brand-blue);font-weight:600}

/* Cards */
.card{position:absolute;left:777px;width:259px;height:147px;box-shadow:0 1px 4px rgba(0,0,0,.15)}
.card-front{top:186px;background:var(--card-blue);color:var(--white)}
.card-front .brand{left:0;right:0;top:84px;justify-content:center;color:var(--white);font-size:12.5px}
.card-front .brand .mark{background:var(--white);width:11px;height:11px}
.card-front .sub{position:absolute;left:50px;right:50px;top:104px;display:flex;align-items:center;gap:6px;font-size:8px;color:var(--white);opacity:.9}
.card-front .sub::before,.card-front .sub::after{content:"";flex:1;height:1px;background:var(--white);opacity:.7}
.card-front .web{position:absolute;left:0;right:0;top:124px;text-align:center;font-size:7.6px}

.card-back{top:400px;background:linear-gradient(135deg,var(--white) 40%,#eaeefb)}
.card-back .brand{left:150px;top:46px;font-size:8px}
.card-back .brand .mark{width:8px;height:8px}
.card-back .sub{position:absolute;left:150px;top:58px;width:95px;display:flex;align-items:center;gap:4px;font-size:6px;color:var(--muted)}
.card-back .sub::before,.card-back .sub::after{content:"";flex:1;height:1px;background:var(--muted)}
.holder{position:absolute;left:17px;top:45px}
.holder .name{color:var(--brand-blue);font-size:9.6px;letter-spacing:.2px}
.holder .role{font-size:7.4px;color:var(--muted);margin-top:1px}
.holder .rule{width:16px;height:1px;background:var(--brand-blue);margin:7px 0 6px}
.contact{font-size:7px;line-height:10.2px;color:var(--muted)}
.contact b{display:inline-block;width:11px;color:var(--brand-blue);font-weight:600}
.contact .addr{margin-top:3px}
</style>
</head>
<body>
<main class="stage">

  <article class="letterhead">
    <div class="brand"><span class="mark"></span>ALDER CREST LAW, LLC</div>

    <section class="team team-a">
      <div class="rule"></div>
      <div class="member">Marion LESTRADE<br>Avocat Associé</div>
      <div class="member">Claire VAUTRIN MALLET<br>Avocat Associé</div>
      <div class="member">Sabine ROCHER<br>Avocat Collaborateur</div>
    </section>
    <section class="team team-b">
      <div class="rule"></div>
      <div class="member">Marion LESTRADE<br>Avocat Associé</div>
      <div class="member">Claire VAUTRIN MALLET<br>Avocat Associé</div>
      <div class="member">Sabine ROCHER<br>Avocat Collaborateur</div>
    </section>

    <section class="letter">
      <div class="salutation">Lorem Ipsum,</div>
      <p>Cras mattis consectetur purus sit amet fermentum. Etiam porta sem malesuada magna mollis euismod. Integer posuere erat a ante venenatis dapibus posuere velit aliquet. Cras justo odio, dapibus ac facilisis in, egestas eget quam. Aenean eu leo quam. Pellentesque ornare sem lacinia quam venenatis vestibulum.</p>
      <p>Vivamus sagittis lacus vel augue laoreet rutrum faucibus dolor auctor. Donec sed odio dui. Etiam porta sem malesuada magna mollis euismod. Morbi leo risus, porta ac consectetur ac, vestibulum at eros. Nullam id dolor id nibh ultricies vehicula ut id elit.</p>
      <p>Cras mattis consectetur purus sit amet fermentum. Etiam porta sem malesuada magna mollis euismod. Integer posuere erat a ante venenatis dapibus posuere velit aliquet. Cras justo odio, dapibus ac facilisis in, egestas eget quam. Aenean eu leo quam. Pellentesque ornare sem lacinia quam venenatis vestibulum.</p>
      <p>Vivamus sagittis lacus vel augue laoreet rutrum faucibus dolor auctor. Donec sed odio dui. Etiam porta sem malesuada magna mollis euismod. Morbi leo risus, porta ac consectetur ac, vestibulum at eros. Nullam id dolor id nibh ultricies vehicula ut id elit.</p>
      <p>Vivamus sagittis lacus vel augue laoreet rutrum faucibus dolor auctor. Donec sed odio dui. Etiam porta sem malesuada magna mollis euismod. Morbi leo risus, porta ac consectetur ac, vestibulum at eros. Nullam id dolor id nibh ultricies vehicula ut id elit.</p>
    </section>

    <footer class="footer">
      <div class="col phones"><strong>Telefon:</strong> (555) 201-4470<br><strong>Fax:</strong> (555) 201-4471</div>
      <div class="col address">880 Juniper Court 4B<br>Larkfield, CO 80999</div>
      <div class="col">info@aldercrestlaw.com<br>www.aldercrestlaw.com</div>
    </footer>
  </article>

  <section class="card card-front">
    <div class="brand"><span class="mark"></span>ALDER CREST</div>
    <div class="sub">LAW, LLC</div>
    <div class="web">www.aldercrestlaw.com</div>
  </section>

  <section class="card card-back">
    <div class="holder">
      <div class="name">NADIA WHITFIELD</div>
      <div class="role">Advocate</div>
      <div class="rule"></div>
      <div class="contact">
        <div><b>T</b>1300 555 018</div>
        <div><b>M</b>(555) 88 412 30 16</div>
        <div><b>E</b>name@aldercrestlaw.com</div>
        <div class="addr">880 Juniper Court 4B<br>Larkfield, CO 80999</div>
      </div>
    </div>
    <div class="brand"><span class="mark"></span>ALDER CREST</div>
    <div class="sub">LAW, LLC</div>
  </section>

</main>
</body>
</html>
```